Veltrom Limited Business Card Design Project

Veltrom Limited is my UK based company used as my brand to work as an Interim Manager or contractor in project/programme management and Non-Executive Director.

Veltrom is Latin for 'execute' as in getting things done rather than killing people!

Logo and design needs to promote reliable, professional, and successful project delivery. Simple, elegant, clean, professional are words that should spring to mind!

Target Market(s)

Middle and senior management in english speaking countries aged 35 - 60 that hire and task qualified and experienced project/programme managers and Non-Executive Directors.

Industry/Entity Type

Contractor

Font styles to use
Serif
Sans Serif

Requirements
Must have
• Mobile telephone number 07842 615509
email address peterhollis@veltrom-example.co.uk
Nice to have
• ProfNet link to my profile.

Interim Manager
Should not have
• avoid Ticks and clocks

```html
<!DOCTYPE html>
<html lang="en">
<head>
<meta charset="utf-8">
<title>Veltrom Limited – Business Card</title>
<link rel="stylesheet" href="https://fonts.googleapis.com/css2?family=Bebas+Neue&family=Lato:wght@400;700;900&display=swap">
<style>
  :root {
    --brand-blue: #1b87c4;
    --brand-blue-deep: #177bb3;
    --charcoal: #404042;
    --charcoal-dark: #38383a;
    --mist: #ececed;
    --paper: #ffffff;
    --ink: #333335;
    --page: #f2f2f2;
  }
  * { box-sizing: border-box; margin: 0; padding: 0; }
  html, body {
    width: 1000px; height: 1200px; overflow: hidden;
    background: var(--page);
  }
  .sheet {
    width: 1000px; height: 1200px;
    display: flex; flex-direction: column; align-items: center; justify-content: center;
    gap: 66px;
  }
  .card {
    position: relative; width: 880px; height: 500px; overflow: hidden;
    box-shadow: 0 2px 6px rgba(0,0,0,.18);
  }
  .card-shapes { position: absolute; inset: 0; width: 100%; height: 100%; }

  /* Front */
  .card-front { background: var(--paper); }
  .brand { position: absolute; left: 68px; top: 76px; }
  .brand-name {
    font-family: "Lato", sans-serif; font-weight: 900; font-size: 40px;
    color: var(--brand-blue); letter-spacing: -0.5px; line-height: 1;
  }
  .brand-slogan {
    font-family: "Lato", sans-serif; font-weight: 400; font-size: 17px;
    color: var(--ink); letter-spacing: 6.5px; margin-top: 6px; padding-left: 6px;
  }
  .holder { position: absolute; left: 68px; top: 313px; color: var(--paper); }
  .holder-name { font-family: "Bebas Neue", sans-serif; font-size: 29px; letter-spacing: .3px; }
  .holder-role { font-family: "Lato", sans-serif; font-size: 15px; margin-left: 8px; }
  .company { position: absolute; left: 68px; top: 383px; color: var(--paper); }
  .company-name { font-family: "Bebas Neue", sans-serif; font-size: 42px; line-height: 1; }
  .company-address { font-family: "Lato", sans-serif; font-weight: 700; font-size: 15px; margin-top: 2px; }
  .contact {
    position: absolute; right: 62px; color: var(--paper); text-align: right;
    font-family: "Lato", sans-serif; font-size: 16px; line-height: 26px;
  }
  .contact-phone { top: 314px; }
  .contact-web { top: 390px; }

  /* Back */
  .card-back { background: var(--charcoal); }
  .back-panel {
    position: absolute; left: 63px; top: 57px; width: 754px; height: 388px;
    background: var(--brand-blue-deep); border: 2px solid var(--charcoal-dark);
    display: flex; flex-direction: column; align-items: center; justify-content: center;
    color: var(--paper);
  }
  .back-name {
    font-family: "Lato", sans-serif; font-weight: 700; font-size: 44px; line-height: 1; margin-top: 12px;
  }
  .back-slogan {
    font-family: "Lato", sans-serif; font-size: 18px; letter-spacing: 7px; margin-top: 8px; padding-left: 7px;
  }
</style>
</head>
<body>
<main class="sheet">
  <section class="card card-front" aria-label="Business card front">
    <svg class="card-shapes" viewBox="0 0 880 500" preserveAspectRatio="none" aria-hidden="true">
      <path fill="var(--mist)" d="M0 252 Q 520 232 880 96 L880 162 Q 460 258 0 266 Z"/>
      <path fill="var(--brand-blue)" d="M0 266 Q 460 258 880 162 L880 234 Q 460 284 0 292 Z"/>
      <path fill="var(--charcoal)" d="M0 292 Q 460 284 880 234 L880 500 L0 500 Z"/>
    </svg>
    <div class="brand">
      <p class="brand-name">Veltrom Limited</p>
      <p class="brand-slogan">Reliable Project Delivery</p>
    </div>
    <p class="holder"><span class="holder-name">PETER HOLLIS</span><span class="holder-role">interim manager</span></p>
    <div class="company">
      <p class="company-name">VELTROM LIMITED</p>
      <p class="company-address">14 Aldgate Row, London EC3N 1AB</p>
    </div>
    <div class="contact contact-phone">
      <p>07842 615509</p>
      <p>Mobile</p>
    </div>
    <div class="contact contact-web">
      <p>peterhollis@veltrom-example.co.uk</p>
      <p>profnet-example.com/peterhollis</p>
    </div>
  </section>

  <section class="card card-back" aria-label="Business card back">
    <div class="back-panel">
      <p class="back-name">Veltrom Limited</p>
      <p class="back-slogan">Reliable Project Delivery</p>
    </div>
  </section>
</main>
</body>
</html>
```